Events & Entertainment Production Coordination Business Cards

We need a business card for a new company based in Los Angeles called "Bright Stage Works"
Our company brings people together for events and helps coordinate different productions. We bring artists from a different country to perform or do events in the U.S.
We are looking for something fun, lively, colorful, creative, and simple.
Nothing that looks too crisp, dark, stiff, or modern.
We connect people from different parts of the world, so definitely something eye-catching will be great!
Colors we would like to see are Black, Yellow, Red, White, Brown to name a few. (Feel free to use more!)
(Double-sided is an option also)
Industry/Entity Type
Business
Contact Information for Business Card
Contact Information to put on Business Card:
Name
Title
Address - 2 lines
Phone - place for 3 numbers
E-mail
URL
Look and feel

```html
<!DOCTYPE html>
<html lang="en">
<head>
<meta charset="utf-8">
<title>Bright Stage Works – Business Card</title>
<link href="https://fonts.googleapis.com/css2?family=Montserrat:wght@400;500;600;700&display=swap" rel="stylesheet">
<style>
  :root {
    --stage-bg: #26282c;
    --brand-red: #8f1b20;
    --card-white: #ffffff;
    --ink: #111111;
  }
  * { margin: 0; padding: 0; box-sizing: border-box; }
  html, body { width: 1200px; height: 900px; overflow: hidden; background: var(--stage-bg); }
  body { position: relative; font-family: "Montserrat", sans-serif; }

  .card { position: absolute; left: 250px; width: 700px; height: 400px; overflow: hidden; }
  .card-back { top: 30px; background: var(--brand-red); }
  .card-front { top: 470px; background: var(--card-white); }

  /* Back side */
  .back-brand { position: absolute; left: 200px; top: 95px; display: flex; align-items: center; gap: 22px; }
  .brand-dot { width: 74px; height: 74px; border-radius: 50%; flex: none; }
  .back-brand .brand-dot { background: var(--card-white); }
  .brand-name { font-weight: 600; font-size: 46px; line-height: 1.05; letter-spacing: 0.5px; }
  .back-brand .brand-name { color: var(--card-white); }
  .back-rule { position: absolute; left: 0; right: 0; top: 262px; display: flex; align-items: center; gap: 14px; }
  .back-rule .line { flex: 1; height: 1.5px; background: var(--card-white); }
  .website { color: var(--card-white); font-size: 15px; font-weight: 500; letter-spacing: 0.3px; }

  /* Front side */
  .front-brand { position: absolute; left: 70px; top: 90px; display: flex; align-items: center; gap: 20px; }
  .front-brand .brand-dot { background: var(--brand-red); width: 80px; height: 80px; }
  .front-brand .brand-name { color: var(--ink); font-size: 44px; }

  .name-tag { position: absolute; right: 0; top: 40px; width: 250px; background: var(--brand-red); color: var(--card-white); padding: 12px 18px; }
  .employee-name { font-weight: 700; font-size: 20px; }
  .employee-title { font-size: 13px; font-weight: 400; margin-top: 2px; }
  .email { position: absolute; right: 22px; top: 122px; font-size: 14px; color: var(--ink); }

  .contact-rail { position: absolute; left: 0; right: 0; top: 226px; height: 3px; background: var(--brand-red); }
  .contact-item { position: absolute; top: 207px; display: flex; flex-direction: column; align-items: center; gap: 8px; }
  .contact-item.mobile { left: 90px; }
  .contact-item.phone { left: 310px; }
  .contact-item.fax { left: 530px; }
  .icon-badge { width: 42px; height: 42px; border-radius: 50%; background: var(--brand-red); display: flex; align-items: center; justify-content: center; }
  .icon-badge svg { width: 22px; height: 22px; }
  .number { font-size: 17px; color: var(--ink); letter-spacing: 0.3px; }

  .address-band { position: absolute; left: 0; right: 0; bottom: 0; height: 92px; background: var(--brand-red); display: flex; align-items: center; justify-content: center; }
  .address { color: var(--card-white); font-size: 18px; letter-spacing: 0.3px; }
</style>
</head>
<body>

<section class="card card-back">
  <div class="back-brand">
    <span class="brand-dot"></span>
    <span class="brand-name">Bright Stage<br>Works</span>
  </div>
  <div class="back-rule">
    <span class="line"></span>
    <span class="website">www.brightstageworks.com</span>
    <span class="line"></span>
  </div>
</section>

<section class="card card-front">
  <div class="front-brand">
    <span class="brand-dot"></span>
    <span class="brand-name">Bright Stage<br>Works</span>
  </div>

  <div class="name-tag">
    <div class="employee-name">Employee Name</div>
    <div class="employee-title">Managing Director</div>
  </div>
  <div class="email">hello@brightstageworks.com</div>

  <div class="contact-rail"></div>

  <div class="contact-item mobile">
    <span class="icon-badge">
      <svg viewBox="0 0 24 24" fill="none" stroke="#fff" stroke-width="2"><rect x="7" y="2" width="10" height="20" rx="2"/><line x1="10" y1="18" x2="14" y2="18"/></svg>
    </span>
    <span class="number">123-456-7890</span>
  </div>

  <div class="contact-item phone">
    <span class="icon-badge">
      <svg viewBox="0 0 24 24" fill="#fff"><path d="M6.6 10.8a15 15 0 0 0 6.6 6.6l2.2-2.2a1 1 0 0 1 1-.25 11.4 11.4 0 0 0 3.6.57 1 1 0 0 1 1 1V20a1 1 0 0 1-1 1A17 17 0 0 1 3 4a1 1 0 0 1 1-1h3.5a1 1 0 0 1 1 1c0 1.25.2 2.45.57 3.57a1 1 0 0 1-.25 1z"/></svg>
    </span>
    <span class="number">123-456-7890</span>
  </div>

  <div class="contact-item fax">
    <span class="icon-badge">
      <svg viewBox="0 0 24 24" fill="none" stroke="#fff" stroke-width="2"><rect x="7" y="3" width="10" height="6"/><rect x="3" y="9" width="18" height="8" rx="1"/><rect x="7" y="14" width="10" height="7" fill="#8f1b20"/></svg>
    </span>
    <span class="number">123-456-7890</span>
  </div>

  <div class="address-band">
    <span class="address">0123 Sample Avenue Los Angeles, CA 00000</span>
  </div>
</section>

</body>
</html>
```